Full service meeting planning company needs new business cards

Velmora Linkway is a full service meeting planning company that specializes in on-line conference registration web development and event communications. We combine citywide hotel management, mobile applications, eblast reminders, confirmation letters, and customized reporting to create a seamless registration process. We also manage group motor coach transportation, food and beverages, entertainment, stage and lighting for group of 10 to 4000.

Target Market(s)

Corporations and associations

Industry/Entity Type

Event Planning

Contact Information for Business Card

standard size 3.5" wide and 2" tall

Font styles to use
Serif
Sans Serif

Colors
f37122
f78f20
333333
5c5c5c
9d9d9d
f68d4d

Requirements
Must have
• {name}
• Velmora Linkway
• P.O. Box 7384, Grand Rapids, M I 49568
• www.velmoralinkway.com
• {email}
• {phone}
• {mobile phone}
Nice to have
• Our colors are black, grey and orange as an accent color
Should not have
• I am not happy with our website layout anymore either. It feels dark and old but it does explain who we are pretty well if you'd like to review; www.velmoralinkway.com

```html
<!DOCTYPE html>
<html lang="en">
<head>
<meta charset="utf-8">
<title>Velmora Linkway — Business Card</title>
<link rel="stylesheet" href="https://fonts.googleapis.com/css2?family=Mulish:wght@400;700;800&display=swap">
<style>
  :root {
    --backdrop: #5a4535;
    --card: #262626;
    --pattern: #2d2d2d;
    --ink: #ffffff;
    --ink-soft: #e6e6e6;
    --accent: #f37122;
    --accent-light: #f78f20;
  }
  html, body {
    margin: 0;
    padding: 0;
    width: 1200px;
    height: 987px;
    overflow: hidden;
    background: var(--backdrop);
    font-family: "Mulish", Arial, sans-serif;
  }
  .canvas {
    position: relative;
    width: 1200px;
    height: 987px;
  }
  .card {
    position: absolute;
    left: 293px;
    width: 615px;
    height: 349px;
    background: var(--card);
    overflow: hidden;
    box-shadow: 0 3px 10px rgba(0,0,0,0.35);
  }
  .card--front { top: 131px; }
  .card--back { top: 506px; }

  .brand-mark {
    position: absolute;
    left: 99px;
    top: 25px;
    width: 110px;
    height: 110px;
    border-radius: 50%;
    background: var(--ink);
  }
  .brand-name {
    position: absolute;
    left: 40px;
    top: 138px;
    margin: 0;
    color: var(--ink);
    font-size: 21px;
    font-weight: 800;
    letter-spacing: 0.2px;
    text-transform: uppercase;
  }
  .address {
    position: absolute;
    left: 40px;
    top: 176px;
    margin: 0;
    color: var(--ink-soft);
    font-style: normal;
    font-size: 16.5px;
    line-height: 21px;
  }
  .address .company {
    font-weight: 700;
    color: var(--ink);
  }
  .contacts {
    position: absolute;
    left: 40px;
    top: 246px;
    margin: 0;
    padding: 0;
    list-style: none;
    color: var(--ink-soft);
    font-size: 16.5px;
    line-height: 22px;
  }
  .contacts li {
    display: flex;
    align-items: center;
    gap: 8px;
  }
  .contacts svg {
    width: 16px;
    height: 16px;
    fill: var(--accent);
    flex: none;
  }
  .person {
    position: absolute;
    right: 27px;
    top: 240px;
    text-align: right;
    color: var(--ink);
  }
  .person-name {
    margin: 0;
    font-size: 21px;
    font-weight: 800;
    line-height: 26px;
  }
  .person-title {
    margin: 0;
    font-size: 17px;
    line-height: 22px;
    color: var(--accent-light);
  }
  .accent-bar {
    position: absolute;
    left: 606px;
    top: 243px;
    width: 9px;
    height: 47px;
    background: var(--accent);
  }

  .back-pattern {
    position: absolute;
    inset: 0;
    background: var(--pattern);
  }
  .back-mark {
    position: absolute;
    border-radius: 50%;
    background: var(--ink);
  }
  .back-mark--center { left: 276px; top: 142px; width: 58px; height: 58px; background: var(--accent); }
  .back-mark--edge-left { left: -20px; top: 30px; width: 58px; height: 58px; }
  .back-mark--edge-right { left: 586px; top: 252px; width: 58px; height: 58px; }
</style>
</head>
<body>
<main class="canvas">
  <section class="card card--front" aria-label="Business card front">
    <div class="brand-mark"></div>
    <h1 class="brand-name">Velmora Linkway</h1>
    <address class="address">
      <span class="company">Velmora Linkway</span><br>
      P.O. Box 7384<br>
      Grand Rapids, M I 49568
    </address>
    <ul class="contacts">
      <li>
        <svg viewBox="0 0 16 16" aria-hidden="true"><path d="M3.6 1.2l2.3 2.6-1.3 1.9c.9 2 2.5 3.6 4.6 4.6l1.9-1.3 2.6 2.3-1.3 2.6C7.3 13.6 2.4 8.7 1.1 3.5z"/></svg>
        (616) 555-0148
      </li>
      <li>
        <svg viewBox="0 0 16 16" aria-hidden="true"><path d="M4 0h8a1 1 0 011 1v14a1 1 0 01-1 1H4a1 1 0 01-1-1V1a1 1 0 011-1zm1 2v10h6V2zm3 11a1 1 0 100 2 1 1 0 000-2z"/></svg>
        (836) 555-0192
      </li>
      <li>
        <svg viewBox="0 0 16 16" aria-hidden="true"><path d="M1 4h14v9H1zm1 1v.3l6 4 6-4V5z"/></svg>
        hello@velmoralinkway.com
      </li>
      <li>
        <svg viewBox="0 0 16 16" aria-hidden="true"><path d="M8 1a7 7 0 100 14A7 7 0 008 1zm0 1.5c.8 0 1.7 1.4 2.1 3.5H5.9C6.3 3.9 7.2 2.5 8 2.5zM2.6 7h2.2a13 13 0 000 2H2.6a5.5 5.5 0 010-2zm3.3 0h4.2a12 12 0 010 2H5.9a12 12 0 010-2zm5.3 0h2.2a5.5 5.5 0 010 2h-2.2a13 13 0 000-2zM5.9 10h4.2c-.4 2.1-1.3 3.5-2.1 3.5S6.3 12.1 5.9 10z"/></svg>
        www.velmoralinkway.com
      </li>
    </ul>
    <div class="person">
      <p class="person-name">ARDEN PELLOWAY</p>
      <p class="person-title">CEO/FOUNDER</p>
    </div>
    <div class="accent-bar"></div>
  </section>

  <section class="card card--back" aria-label="Business card back">
    <div class="back-pattern" role="img" aria-label="Subtle repeating brand pattern in dark grey"></div>
    <div class="back-mark back-mark--edge-left"></div>
    <div class="back-mark back-mark--center"></div>
    <div class="back-mark back-mark--edge-right"></div>
  </section>
</main>
</body>
</html>
```